Saffron Lantern Court Business Card

I am looking for a business card desgined for my restaurant. It is an Indian restaurant, we are looking for something thats modern, yet traditional with the indian culture, we are looking for colors that match our logo. The logo is a design of the building with the name of the restaurant. for more information on the restaurant go to www.saffronlanterncourt.example

Industry/Entity Type

Indian Restaurant

Contact Information for Business Card

we are looking for somthing thats modern, yet traditional with the indian culture, we are looking for colors that match our logo. The logo is a design of the building with the name of the restaurant. for more information on the restaurant go to www.saffronlanterncourt.example

Requirements
Must have
• The logo that is attached,
• Name: Harvinder Oberoi,
• address of the restaurant: 7328 West Larkspur Rd, Phoenix, Arizona, 85213
• Phone: (602) 555-0147
• Fax: (602) 555-0193
• Restaurant Catering Banquet
• Website: www.SaffronLanternCourt.example
Nice to have
• wanted to get something that goes with the theme of the restaurant, which is traditional but also keep a very professional and modern touch

```html
<!DOCTYPE html>
<html lang="en">
<head>
<meta charset="utf-8">
<title>Saffron Lantern Court Business Card</title>
<link rel="stylesheet" href="https://fonts.googleapis.com/css2?family=Open+Sans:wght@400;600&display=swap">
<style>
  :root {
    --backdrop: #2a2c30;
    --saffron: #f26b21;
    --crimson: #a9262a;
    --brand-red: #c8342b;
    --name-orange: #d9461c;
    --ink: #2b2b2b;
    --paper: #ffffff;
    --cream: #fff7ee;
  }
  * { margin: 0; padding: 0; box-sizing: border-box; }
  html, body {
    width: 1200px;
    height: 864px;
    overflow: hidden;
    background: var(--backdrop);
    font-family: "Open Sans", Arial, sans-serif;
  }
  .stage {
    position: relative;
    width: 1200px;
    height: 864px;
  }
  .card {
    position: absolute;
    left: 320px;
    width: 560px;
    height: 320px;
    border-radius: 3px;
    overflow: hidden;
    box-shadow: 0 10px 28px rgba(0, 0, 0, 0.35);
  }
  .card--front {
    top: 80px;
    background: linear-gradient(180deg, var(--saffron) 0%, #e04b23 55%, var(--crimson) 100%);
    display: flex;
    align-items: center;
    justify-content: center;
  }
  .front-wordmark {
    color: var(--cream);
    font-weight: 600;
    font-size: 40px;
    line-height: 1.12;
    letter-spacing: 2px;
    text-align: center;
    text-transform: uppercase;
  }
  .card--back {
    top: 464px;
    background: var(--paper);
    color: var(--ink);
  }
  .contact-name {
    position: absolute;
    left: 36px;
    top: 30px;
    color: var(--name-orange);
    font-weight: 600;
    font-size: 19px;
  }
  .contact-address {
    position: absolute;
    left: 36px;
    top: 66px;
    font-size: 13px;
    line-height: 1.45;
  }
  .contact-lines {
    position: absolute;
    right: 36px;
    top: 108px;
    list-style: none;
    font-size: 13.5px;
    line-height: 1.45;
    text-align: right;
  }
  .contact-lines li {
    display: flex;
    align-items: center;
    justify-content: flex-end;
    gap: 8px;
  }
  .contact-icon {
    width: 11px;
    height: 11px;
    flex: none;
  }
  .back-wordmark {
    position: absolute;
    left: 0;
    right: 0;
    bottom: 40px;
    color: var(--brand-red);
    font-weight: 600;
    font-size: 24px;
    line-height: 1.12;
    letter-spacing: 1.5px;
    text-align: center;
    text-transform: uppercase;
  }
</style>
</head>
<body>
<main class="stage">
  <section class="card card--front" aria-label="Card front">
    <p class="front-wordmark">Saffron<br>Lantern<br>Court</p>
  </section>

  <section class="card card--back" aria-label="Card back">
    <h1 class="contact-name">Harvinder Oberoi</h1>
    <p class="contact-address">7328 West Larkspur Rd,<br>Phoenix, Arizona, 85213</p>
    <ul class="contact-lines">
      <li>(602) 555-0147
        <svg class="contact-icon" viewBox="0 0 12 12" aria-hidden="true">
          <path d="M2.5 1 L4.5 1 L5.3 3.6 L4 4.6 Q5 7 7.4 8 L8.4 6.7 L11 7.5 L11 9.5 Q11 11 9.5 11 Q1 10 1 2.5 Q1 1 2.5 1 Z" fill="var(--brand-red)"/>
        </svg>
      </li>
      <li>(602) 555-0193
        <svg class="contact-icon" viewBox="0 0 12 12" aria-hidden="true">
          <rect x="3" y="1" width="6" height="4" fill="var(--brand-red)"/>
          <rect x="1" y="5" width="10" height="6" rx="1" fill="var(--brand-red)"/>
        </svg>
      </li>
      <li>www.SaffronLanternCourt.example
        <svg class="contact-icon" viewBox="0 0 12 12" aria-hidden="true">
          <circle cx="6" cy="6" r="5.5" fill="var(--brand-red)"/>
          <path d="M6 .5 V11.5 M.5 6 H11.5" stroke="var(--paper)" stroke-width="1"/>
        </svg>
      </li>
    </ul>
    <p class="back-wordmark">Saffron<br>Lantern<br>Court</p>
  </section>
</main>
</body>
</html>
```